MoveNest Landing Page

We need to freshen up our homepage.

The company is MoveNest.com. We provide cloud-based management software for class venues - dance, yoga, martial arts, etc.

The challenge here is to create something that's simultaneously lighthearted and professional. We want our customers to know that the software is easy, fun and non-intimidating, but also powerful enough to handle whatever they throw at it.

Page content can remain the same as it is now. Feel free to move things around, manipulate it however you like.

We like our logo, but feel free to manipulate it as part of your design. Fonts used in the logo are Futura Extra Bold and Rockwell.

NOTE: The default screenshot in the homepage video is NOT our branding choice, it just happens to be the default freeze frame from vidloop.. Feel free to ignore it altogether in your design. We are not affiliated with that character, or the app that we used to create the vid.
Updates

Project Deadline Extended
Reason: We are extending this contest by request. Out of 65 designs, so far we only really like 4. There's still a good chance to win this contract! Please submit your very best :) Owen

Target Market(s)

Studio owners who are not necessarily tech savvy.

Industry/Entity Type

Software

Requirements
Must have
• Look and feel of a modern web app.

Delivery in a layered PSD.

```html
<!DOCTYPE html>
<html lang="en">
<head>
<meta charset="utf-8">
<title>MoveNest – Manage your classes online</title>
<link href="https://fonts.googleapis.com/css2?family=Open+Sans:wght@300;400;600;700;800&family=Dancing+Script:wght@600&display=swap" rel="stylesheet">
<style>
:root{
  --blue:#56759f;
  --blue-light:#83a9df;
  --green:#6edb0a;
  --green-line:#68d400;
  --text:#5a5a5a;
  --muted:#8a8a8a;
  --grey-bg:#f1f1f1;
  --rule:#e6e6e6;
  --white:#ffffff;
  --dark:#1e1e1e;
}
*{margin:0;padding:0;box-sizing:border-box}
html,body{width:866px;height:1200px;overflow:hidden;background:var(--white)}
body{position:relative;font-family:"Open Sans",Arial,sans-serif;color:var(--text)}
a{text-decoration:none;color:inherit}
ul{list-style:none}

/* header */
.site-header{position:absolute;left:0;top:0;width:866px;height:86px;background:var(--white)}
.brand{position:absolute;left:116px;top:24px;font-weight:800;font-size:29px;color:var(--blue);letter-spacing:-0.5px;line-height:36px}
.main-nav{position:absolute;left:515px;top:32px;height:26px;display:flex;align-items:center;font-size:10px;font-weight:700;color:var(--blue)}
.main-nav a{padding:0 12px;border-left:1px solid #d4d4d4;line-height:12px}
.main-nav a:first-child{padding-left:0;border-left:none}
.main-nav a:nth-child(3){padding-right:0}
.btn-start{position:absolute;left:662px;top:31px;width:88px;height:27px;background:var(--green);color:var(--white);font-size:9.5px;font-weight:700;display:flex;align-items:center;justify-content:center}

/* hero */
.hero{position:absolute;left:0;top:86px;width:866px;height:274px;overflow:hidden}
.hero-photo{position:absolute;inset:0;background:
  radial-gradient(ellipse 180px 150px at 195px 170px,#9ca6b8 0%,rgba(120,130,150,0.5) 60%,rgba(0,0,0,0) 100%),
  radial-gradient(ellipse 300px 160px at 600px 60px,#7e9c96 0%,rgba(60,80,80,0) 100%),
  linear-gradient(90deg,#1c2422 0%,#46544f 30%,#5f716d 55%,#4a5754 80%,#2f3836 100%)}
.hero-copy{position:absolute;left:433px;top:50px;color:var(--white)}
.hero-title{font-size:14.5px;font-weight:700;line-height:22.5px;text-transform:uppercase;letter-spacing:0.1px}
.features{position:absolute;left:0;top:59px;width:330px;display:grid;grid-template-columns:163px 167px;row-gap:4px;font-size:9.8px;line-height:14.5px}
.features li{display:flex;align-items:center;gap:7px;white-space:nowrap}
.features b{font-weight:700}
.tick{width:9px;height:8px;flex:none}
.btn-setup{position:absolute;left:0;top:134px;width:123px;height:33px;background:var(--green);color:var(--white);font-size:11px;font-weight:700;display:flex;align-items:center;justify-content:center}
.free-note{position:absolute;left:137px;top:139px;font-family:"Dancing Script",cursive;font-size:15px;color:var(--white);white-space:nowrap}

/* about */
.about-title{position:absolute;left:116px;top:421px;font-size:19px;font-weight:300;color:#666;letter-spacing:0.2px}
.about-title strong{font-weight:700;color:var(--blue)}
.about-text{position:absolute;left:116px;top:456px;width:350px;font-size:9.6px;line-height:14.2px;color:var(--text)}
.video{position:absolute;left:508px;top:390px;width:242px;height:152px;background:var(--blue-light)}
.video-controls{position:absolute;left:0;bottom:0;width:242px;height:33px;background:var(--dark)}
.video svg{position:absolute}

/* pricing */
.pricing{position:absolute;left:0;top:565px;width:866px;height:495px;background:var(--grey-bg)}
.plan{position:absolute;top:45px;width:198px;height:325px;background:var(--white);border:1px solid #e2e2e2;border-bottom:4px solid var(--green-line)}
.plan-name{margin-top:20px;text-align:center;font-size:19px;font-weight:400;color:var(--blue);line-height:22px}
.plan-price{text-align:center;font-size:18px;font-weight:700;color:var(--blue);line-height:22px}
.plan-price span{font-size:12px;font-weight:400}
.plan-features{margin:9px 9px 0 9px}
.plan-features li{height:20.4px;border-bottom:1px solid var(--rule);display:flex;align-items:center;gap:6px;padding-left:9px;font-size:8.8px;color:#666;white-space:nowrap}
.plan-features li:last-child{border-bottom:none}
.plan-features .tick{width:8px;height:7px}
.trial{position:absolute;left:0;top:397px;width:866px;text-align:center;font-size:15px;color:var(--blue);font-weight:400}
.btn-mail{position:absolute;left:366px;top:428px;width:134px;height:29px;background:var(--green);color:var(--white);font-size:11.5px;display:flex;align-items:center;justify-content:center}

/* footer */
.site-footer{position:absolute;left:0;top:1060px;width:866px;height:140px;background:var(--white)}
.footer-links{position:absolute;top:40px;font-size:8.8px;color:#777}
.footer-links li{height:18.5px;display:flex;align-items:center;gap:6px}
.caret{width:3px;height:6px;flex:none}
.newsletter-label{position:absolute;left:354px;top:41px;font-size:12px;color:#888}
.newsletter{position:absolute;left:354px;top:61px;display:flex}
.newsletter-input{width:148px;height:25px;background:#efefef;font-size:8.5px;color:#aaa;padding-left:15px;display:flex;align-items:center}
.btn-subscribe{width:68px;height:25px;background:var(--green);color:var(--white);font-size:10px;display:flex;align-items:center;justify-content:center}
.footer-brand{position:absolute;left:609px;top:62px;font-weight:800;font-size:24px;color:var(--blue);letter-spacing:-0.5px;line-height:30px}
.stripe{position:absolute;left:0;bottom:0;width:866px;height:3px;background:repeating-linear-gradient(90deg,var(--blue) 0 25px,var(--green) 25px 75px,var(--blue) 75px 100px)}
</style>
</head>
<body>

<svg width="0" height="0" style="position:absolute">
  <defs>
    <symbol id="tick" viewBox="0 0 10 8"><path d="M1 4.2 L3.8 7 L9 1" fill="none" stroke="currentColor" stroke-width="2"/></symbol>
    <symbol id="caret" viewBox="0 0 3 6"><path d="M0 0 L3 3 L0 6 Z" fill="currentColor"/></symbol>
  </defs>
</svg>

<header class="site-header">
  <div class="brand">MoveNest</div>
  <nav class="main-nav">
    <a href="#">HOME</a>
    <a href="#">LOGIN</a>
    <a href="#">HELP</a>
  </nav>
  <a class="btn-start" href="#">GET STARTED!</a>
</header>

<section class="hero">
  <div class="hero-photo" role="img" aria-label="Blurred office background with a young man in glasses pulling open his shirt to reveal a purple emblem"></div>
  <div class="hero-copy">
    <h1 class="hero-title">The easiest way to manage your<br>classes and accept payments online.</h1>
    <ul class="features">
      <li><svg class="tick" style="color:#fff"><use href="#tick"/></svg><span><b>WEB BASED,</b> login anywhere</span></li>
      <li><svg class="tick" style="color:#fff"><use href="#tick"/></svg><span><b>SECURE,</b> your info is super safe</span></li>
      <li><svg class="tick" style="color:#fff"><use href="#tick"/></svg><span><b>INTUITIVE,</b> easy to use</span></li>
      <li><svg class="tick" style="color:#fff"><use href="#tick"/></svg><span><b>VERSATILE,</b> it's for class venue</span></li>
      <li><svg class="tick" style="color:#fff"><use href="#tick"/></svg><span><b>ROBUST,</b> fast and powerful</span></li>
      <li><svg class="tick" style="color:#fff"><use href="#tick"/></svg><span><b>AFFORDABLE,</b> free version</span></li>
    </ul>
    <a class="btn-setup" href="#">5 MINUTE SETUP!</a>
    <span class="free-note">it's free</span>
  </div>
</section>

<section class="about">
  <h2 class="about-title">WHAT IS <strong>MOVENEST ?</strong></h2>
  <p class="about-text">MoveNest is the easiest and most affordable way to manage your class studio or venue. We help simplify your daily tasks by leveraging the power of the internet, saving you time and money. Anyone can learn to use MoveNest with our clean, common-sense website.</p>
  <div class="video">
    <svg width="48" height="48" style="left:97px;top:42px" viewBox="0 0 48 48">
      <circle cx="24" cy="24" r="22" fill="none" stroke="#a9c4ea" stroke-width="2"/>
      <path d="M20 17 L30 24 L20 31 Z" fill="#c4d6f0"/>
    </svg>
    <div class="video-controls">
      <svg width="242" height="33" viewBox="0 0 242 33" style="left:0;top:0">
        <rect x="0" y="0" width="32" height="33" fill="#111"/>
        <rect x="12" y="11" width="3" height="10" fill="#fff"/>
        <rect x="17" y="11" width="3" height="10" fill="#fff"/>
        <rect x="44" y="15" width="164" height="4" rx="2" fill="#3a3a3a"/>
        <rect x="44" y="15" width="53" height="4" rx="2" fill="#6a8bb8"/>
        <circle cx="84" cy="17" r="2.5" fill="#fff"/>
        <path d="M222 14 h3 l4 -3 v12 l-4 -3 h-3 z" fill="#fff"/>
        <path d="M231 13 q3 4 0 8" fill="none" stroke="#fff" stroke-width="1.2"/>
      </svg>
    </div>
  </div>
</section>

<section class="pricing">
  <article class="plan" style="left:117px">
    <h3 class="plan-name">Standard</h3>
    <p class="plan-price">FREE!</p>
    <ul class="plan-features">
      <li><svg class="tick" style="color:#666"><use href="#tick"/></svg>Fully functional scheduling tool</li>
      <li><svg class="tick" style="color:#666"><use href="#tick"/></svg>Filters for easy viewing</li>
      <li><svg class="tick" style="color:#666"><use href="#tick"/></svg>Web Based: Login Anywhere</li>
      <li><svg class="tick" style="color:#666"><use href="#tick"/></svg>Track students &amp; instructors</li>
      <li><svg class="tick" style="color:#666"><use href="#tick"/></svg>Store/access Customer Info</li>
      <li><svg class="tick" style="color:#666"><use href="#tick"/></svg>Notekeeping &amp; Attendance</li>
      <li><svg class="tick" style="color:#666"><use href="#tick"/></svg>SSL security</li>
      <li><svg class="tick" style="color:#666"><use href="#tick"/></svg>Regular data backups</li>
      <li><svg class="tick" style="color:#666"><use href="#tick"/></svg>1 User account</li>
      <li><svg class="tick" style="color:#666"><use href="#tick"/></svg>E-mail support</li>
      <li><svg class="tick" style="color:#666"><use href="#tick"/></svg>No Credit Card Required</li>
    </ul>
  </article>
  <article class="plan" style="left:334px">
    <h3 class="plan-name">Premium</h3>
    <p class="plan-price">$39<span>/Month</span></p>
    <ul class="plan-features">
      <li><svg class="tick" style="color:#666"><use href="#tick"/></svg>3 User Accounts</li>
      <li><svg class="tick" style="color:#666"><use href="#tick"/></svg>Simultaneous Logins</li>
      <li><svg class="tick" style="color:#666"><use href="#tick"/></svg>Collaboration: File Sharing &amp; Storage</li>
      <li><svg class="tick" style="color:#666"><use href="#tick"/></svg>Activity Feed: Track your efforts</li>
      <li><svg class="tick" style="color:#666"><use href="#tick"/></svg>Activity Feed: Discussion Board</li>
      <li><svg class="tick" style="color:#666"><use href="#tick"/></svg>Attendance Sheets</li>
      <li><svg class="tick" style="color:#666"><use href="#tick"/></svg>Instructor Work Histories &amp; Schedules</li>
      <li><svg class="tick" style="color:#666"><use href="#tick"/></svg>Customer Histories &amp; Schedules</li>
      <li><svg class="tick" style="color:#666"><use href="#tick"/></svg>1 User account</li>
      <li><svg class="tick" style="color:#666"><use href="#tick"/></svg>E-mail support</li>
      <li><svg class="tick" style="color:#666"><use href="#tick"/></svg>Best in Class Phone Support</li>
    </ul>
  </article>
  <article class="plan" style="left:552px">
    <h3 class="plan-name">Premium</h3>
    <p class="plan-price">$79<span>/Month</span></p>
    <ul class="plan-features">
      <li><svg class="tick" style="color:#666"><use href="#tick"/></svg>Powerful Point of Sale System</li>
      <li><svg class="tick" style="color:#666"><use href="#tick"/></svg>Accept Credit Cards Immediately</li>
      <li><svg class="tick" style="color:#666"><use href="#tick"/></svg>Web Store: Sell Your Classes Online</li>
      <li><svg class="tick" style="color:#666"><use href="#tick"/></svg>Easily Publish Your Schedule Online</li>
      <li><svg class="tick" style="color:#666"><use href="#tick"/></svg>Sell Retail Goods, Tickets, and More</li>
      <li><svg class="tick" style="color:#666"><use href="#tick"/></svg>MailBeacon Integration</li>
      <li><svg class="tick" style="color:#666"><use href="#tick"/></svg>LedgerLeaf Integration</li>
      <li><svg class="tick" style="color:#666"><use href="#tick"/></svg>Add User Accounts for $5</li>
      <li><svg class="tick" style="color:#666"><use href="#tick"/></svg>Priority Customer Support</li>
    </ul>
  </article>
  <p class="trial">Ask about a free 30 day trial</p>
  <a class="btn-mail" href="#">Info@movenest.com</a>
</section>

<footer class="site-footer">
  <ul class="footer-links" style="left:116px">
    <li><svg class="caret" style="color:#777"><use href="#caret"/></svg>Home</li>
    <li><svg class="caret" style="color:#777"><use href="#caret"/></svg>Login</li>
    <li><svg class="caret" style="color:#777"><use href="#caret"/></svg>Help</li>
  </ul>
  <ul class="footer-links" style="left:228px">
    <li><svg class="caret" style="color:#777"><use href="#caret"/></svg>Features</li>
    <li><svg class="caret" style="color:#777"><use href="#caret"/></svg>More video</li>
    <li><svg class="caret" style="color:#777"><use href="#caret"/></svg>Contact us</li>
  </ul>
  <p class="newsletter-label">News Letter</p>
  <form class="newsletter">
    <div class="newsletter-input">E-mail Address :</div>
    <div class="btn-subscribe">Subscribe</div>
  </form>
  <div class="footer-brand">MoveNest</div>
  <div class="stripe"></div>
</footer>

</body>
</html>
```